Next-Gen B2B Sales Negotiation App - UI Design for iOS

Develop a user-friendly dark-mode interface for a B2B sales negotiation assistant app for a company called Quorvel. The UI will showcase a single screen with features like counterparty search, agenda selection, and email drafting. Design should reflect a functional iOS app with realistic placeholder data to create a genuine experience.

Precise task description in attachment.

Target Market(s)

B2B

Requirements
Must have
• Each UI picture should look like a screen capture of an iphone
Nice to have
• The UI designs need to show the navigation and the app in use

```html
<!DOCTYPE html>
<html lang="en">
<head>
<meta charset="utf-8">
<title>Quorvel – B2B Sales Negotiation App</title>
<link rel="stylesheet" href="https://fonts.googleapis.com/css2?family=Silkscreen&family=Chakra+Petch:wght@400;500;600&display=swap">
<style>
:root{
  --bg-top:#22102f;
  --bg-bottom:#07040a;
  --screen-top:#1c0c2a;
  --screen-bottom:#060307;
  --card:#140b1c;
  --card-line:#2a1a36;
  --row:#170d20;
  --icon:#5c3c80;
  --text:#f1ecf6;
  --muted:#8d7f9c;
  --cyan:#1ee8f2;
  --violet:#9b6cf0;
  --pink:#f23fd2;
  --accent:#ff4a9b;
  --grey-head:#8a8292;
}
*{box-sizing:border-box;margin:0;padding:0}
html,body{width:1200px;height:2172px;overflow:hidden}
body{
  position:relative;
  background:linear-gradient(180deg,var(--bg-top) 0%,#130a1c 45%,var(--bg-bottom) 100%);
  font-family:"Chakra Petch",sans-serif;color:var(--text);
}
.headline{
  position:absolute;left:0;width:1200px;top:100px;text-align:center;
  font-family:"Silkscreen",monospace;font-size:54px;line-height:88px;letter-spacing:1px;
  background:linear-gradient(90deg,var(--cyan) 28%,var(--violet) 52%,var(--pink) 75%);
  -webkit-background-clip:text;background-clip:text;color:transparent;
}
.section-label{
  position:absolute;left:0;width:1200px;top:316px;text-align:center;
  font-family:"Silkscreen",monospace;font-size:30px;color:var(--grey-head);
}
.closing{
  position:absolute;left:0;width:1200px;top:1928px;text-align:center;
  font-family:"Silkscreen",monospace;font-size:38px;color:#fff;letter-spacing:1px;
}
.screen{
  position:absolute;left:440px;top:453px;width:350px;height:1370px;border-radius:28px;overflow:hidden;
  background:radial-gradient(ellipse at 50% 0%,#3a1450 0%,transparent 40%),linear-gradient(180deg,var(--screen-top),var(--screen-bottom) 60%);
}
.abs{position:absolute}
.menu-btn{left:12px;top:24px;width:36px;height:36px;border-radius:50%;background:#2d1840;display:flex;align-items:center;justify-content:center}
.brand{left:0;width:350px;top:22px;text-align:center;font-size:34px;font-weight:500;color:#fff;letter-spacing:.5px}
.avatar{left:301px;top:24px;width:36px;height:36px;border-radius:50%;background:linear-gradient(180deg,#d9d2cc,#5b4f4a);border:2px solid #fff}
.card{position:absolute;left:19px;width:319px;background:var(--card);border:1px solid var(--card-line);border-radius:14px}
.card-title{
  height:52px;display:flex;align-items:center;justify-content:center;font-size:14px;font-weight:500;letter-spacing:.8px;
  background:linear-gradient(90deg,var(--cyan),var(--violet) 50%,var(--pink));
  -webkit-background-clip:text;background-clip:text;color:transparent;
}
.field{height:59px;background:var(--row);border-top:1px solid var(--card-line);display:flex;align-items:center;padding:0 14px 0 16px;margin-bottom:12px}
.field:last-child{margin-bottom:0;border-radius:0 0 14px 14px}
.field svg.lead{width:24px;height:24px;flex:none}
.field-text{margin-left:18px;flex:1;text-transform:uppercase}
.field-label{font-size:8.5px;color:var(--muted);letter-spacing:.5px}
.field-value{font-size:12px;letter-spacing:.5px;margin-top:3px}
.trail{width:22px;height:22px;border-radius:50%;background:#21142b;display:flex;align-items:center;justify-content:center}
.mode-row{display:flex;gap:16px;padding:0 16px;margin-bottom:14px}
.mode{flex:1;height:47px;border-radius:6px;border:1px solid var(--card-line);display:flex;align-items:center;padding-left:12px;gap:16px;font-size:12px;text-transform:uppercase;color:#cfc6d8}
.mode.active{background:var(--accent);border-color:var(--accent);color:#fff}
.tiles{display:flex;gap:14px;padding:0 16px 18px}
.tile{width:88px;height:76px;border-radius:6px;border:1px solid var(--card-line);display:flex;flex-direction:column;align-items:center;justify-content:center;gap:10px;font-size:12px;text-transform:uppercase;color:#cfc6d8}
.tile.active{background:var(--accent);border-color:var(--accent);color:#fff}
.draft{border-top:1px solid var(--card-line);display:flex;padding:16px 14px 20px 14px;gap:16px}
.draft p{font-size:11.2px;line-height:21.6px;text-transform:uppercase;letter-spacing:.3px}
.btn{position:absolute;top:1225px;height:47px;border-radius:10px;display:flex;align-items:center;justify-content:center;font-size:13px;text-transform:uppercase;letter-spacing:.5px}
.btn-primary{left:19px;width:148px;background:var(--accent);color:#fff;box-shadow:0 6px 18px rgba(255,74,155,.35)}
.btn-secondary{left:191px;width:147px;border:1px solid var(--card-line);background:#0d0810;color:#cfc6d8}
</style>
</head>
<body>
<div class="headline">NEXT-GEN B2B SALES<br>NEGOTIATION APP</div>
<div class="section-label">HOME SCREEN</div>

<main class="screen">
  <div class="abs menu-btn">
    <svg width="16" height="14" viewBox="0 0 16 14"><rect x="1" y="1" width="13" height="2" rx="1" fill="#b48cff"/><rect x="1" y="6" width="9" height="2" rx="1" fill="#f23fd2"/><rect x="1" y="11" width="13" height="2" rx="1" fill="#1ee8f2"/></svg>
  </div>
  <div class="abs brand">quorvel</div>
  <div class="abs avatar" role="img" aria-label="User profile photo"></div>

  <section class="card" style="top:99px">
    <div class="card-title">PLEASE SELECT</div>
    <div class="field">
      <svg class="lead" viewBox="0 0 24 24"><path d="M2 22V8l7-4v18zM10 22V11h5v11zM16 22V7h6v15z" fill="var(--icon)"/></svg>
      <div class="field-text"><div class="field-label">Please select</div><div class="field-value">Company</div></div>
      <div class="trail"><svg width="10" height="6" viewBox="0 0 10 6"><path d="M1 1l4 4 4-4" stroke="#6c5a7c" fill="none" stroke-width="1.3"/></svg></div>
    </div>
    <div class="field">
      <svg class="lead" viewBox="0 0 24 24"><path d="M3 22V4l10-2v20zM14 22V9h7v13z" fill="var(--icon)"/><path d="M6 7h4M6 11h4M6 15h4" stroke="#170d20" stroke-width="1.5"/></svg>
      <div class="field-text"><div class="field-label">Select company name</div><div class="field-value">Lumenfold Studios</div></div>
      <div class="trail"><svg width="10" height="6" viewBox="0 0 10 6"><path d="M1 1l4 4 4-4" stroke="#6c5a7c" fill="none" stroke-width="1.3"/></svg></div>
    </div>
    <div class="field">
      <svg class="lead" viewBox="0 0 24 24"><circle cx="12" cy="7" r="5" fill="var(--icon)"/><path d="M2 22c0-6 4-9 10-9s10 3 10 9z" fill="var(--icon)"/></svg>
      <div class="field-text"><div class="field-label">Select your position</div><div class="field-value">CEO</div></div>
      <div class="trail"><svg width="10" height="6" viewBox="0 0 10 6"><path d="M1 1l4 4 4-4" stroke="#6c5a7c" fill="none" stroke-width="1.3"/></svg></div>
    </div>
  </section>

  <section class="card" style="top:395px">
    <div class="card-title">AGENDA</div>
    <div class="field">
      <svg class="lead" viewBox="0 0 24 24"><rect x="4" y="3" width="16" height="19" rx="3" fill="var(--icon)"/><path d="M8 9h8M8 13h8M8 17h5" stroke="#170d20" stroke-width="1.6"/></svg>
      <div class="field-text"><div class="field-label">Select agenta</div><div class="field-value">Book a meeting</div></div>
      <div class="trail"><svg width="10" height="6" viewBox="0 0 10 6"><path d="M1 1l4 4 4-4" stroke="#6c5a7c" fill="none" stroke-width="1.3"/></svg></div>
    </div>
    <div class="field">
      <svg class="lead" viewBox="0 0 24 24"><circle cx="10" cy="11" r="9" fill="var(--icon)"/><rect x="13" y="13" width="10" height="9" rx="2" fill="var(--icon)" stroke="#170d20"/></svg>
      <div class="field-text"><div class="field-label">Describe meeting duration</div><div class="field-value">30 minutes</div></div>
      <div class="trail"><svg width="12" height="12" viewBox="0 0 12 12"><circle cx="6" cy="6" r="5.5" fill="#6c5a7c"/><path d="M6 3v3l2 1" stroke="#21142b" fill="none"/></svg></div>
    </div>
    <div class="field">
      <svg class="lead" viewBox="0 0 24 24"><rect x="2" y="4" width="20" height="18" rx="4" fill="var(--icon)"/><path d="M2 9h20" stroke="#170d20" stroke-width="1.5"/></svg>
      <div class="field-text"><div class="field-label">Date</div><div class="field-value">February 17, 2025</div></div>
      <div class="trail"><svg width="11" height="11" viewBox="0 0 11 11"><rect x="1" y="2" width="9" height="8" rx="1" fill="#6c5a7c"/></svg></div>
    </div>
    <div class="mode-row">
      <div class="mode active">
        <svg width="24" height="24" viewBox="0 0 24 24"><rect x="2" y="2" width="13" height="20" rx="3" fill="none" stroke="#fff" stroke-width="1.6"/><rect x="13" y="2" width="9" height="7" rx="2" fill="#fff"/></svg>
        Online
      </div>
      <div class="mode">
        <svg width="24" height="24" viewBox="0 0 24 24"><circle cx="12" cy="9" r="4" fill="var(--icon)"/><rect x="2" y="15" width="20" height="4" rx="1" fill="var(--icon)"/><rect x="8" y="1" width="8" height="3" rx="1" fill="var(--icon)"/></svg>
        On-site
      </div>
    </div>
    <div class="field" style="margin-bottom:0">
      <svg class="lead" viewBox="0 0 24 24"><rect x="2" y="4" width="20" height="18" rx="4" fill="var(--icon)"/><path d="M2 9h20" stroke="#170d20" stroke-width="1.5"/></svg>
      <div class="field-text"><div class="field-label">Describe selling points</div><div class="field-value">We can save your time</div></div>
    </div>
  </section>

  <section class="card" style="top:808px">
    <div class="card-title">CONTACT METHOD</div>
    <div class="tiles">
      <div class="tile active">
        <svg width="28" height="20" viewBox="0 0 28 20"><rect x="1" y="1" width="26" height="18" rx="3" fill="#fff"/><path d="M2 3l12 9 12-9" stroke="var(--accent)" stroke-width="2" fill="none"/></svg>
        Email
      </div>
      <div class="tile">
        <svg width="26" height="26" viewBox="0 0 26 26"><rect x="1" y="1" width="24" height="24" rx="3" fill="var(--icon)"/></svg>
        Proline
      </div>
      <div class="tile">
        <svg width="18" height="28" viewBox="0 0 18 28"><rect x="1" y="1" width="16" height="26" rx="3" fill="var(--icon)"/><circle cx="9" cy="22" r="1.5" fill="#140b1c"/></svg>
        Phone
      </div>
    </div>
  </section>

  <section class="card" style="top:979px">
    <div class="card-title">EMAIL DRAFTING</div>
    <div class="draft">
      <svg width="22" height="22" viewBox="0 0 22 22" style="flex:none;margin-top:4px"><rect x="1" y="1" width="14" height="19" rx="2" fill="var(--icon)"/><path d="M4 6h8M4 10h8M4 14h5" stroke="#140b1c" stroke-width="1.4"/><path d="M20 6l-8 12-2 3 1-4 8-12z" fill="var(--icon)" stroke="#140b1c"/></svg>
      <p>Hi Marek, I am reaching out to you as I have a solution to save your money and time. I am kindly proposing a meeting for week 8, for instance on Monday 17 February.<br>Best regards, Elias</p>
    </div>
  </section>

  <div class="btn btn-primary">Send now</div>
  <div class="btn btn-secondary">Schedule</div>
</main>

<div class="closing">THANK YOU FOR WATCHING MY WORK</div>
</body>
</html>
```